Business Card Design

Want something very unique. No business, just personal. The image I submitted is for inspiration only.

Target Market(s)

friends and new acquaintances

Industry/Entity Type

Business

Contact Information for Business Card

Nora Pettigrew
Marrow Creek, NM
505-771-4926
norapettigrew@quillmail.net

```html
<!DOCTYPE html>
<html lang="en">
<head>
<meta charset="utf-8">
<title>Nora Pettigrew — Personal Card</title>
<link href="https://fonts.googleapis.com/css2?family=Great+Vibes&family=Open+Sans:wght@400&display=swap" rel="stylesheet">
<style>
  :root {
    --page-bg: #e9e7e4;
    --band-dark: #3c3d3f;
    --band-mid: #5a5b5e;
    --rule: #dcdcdc;
    --text-light: #ffffff;
    --pattern-light: #f4f4f4;
    --pattern-mid: #9a9a9a;
    --pattern-dark: #4a4a4a;
  }
  html, body {
    margin: 0;
    padding: 0;
    width: 1200px;
    height: 1014px;
    overflow: hidden;
    background: var(--page-bg);
  }
  .canvas {
    position: relative;
    width: 1200px;
    height: 1014px;
    display: flex;
    align-items: center;
    justify-content: center;
  }
  .card {
    position: relative;
    width: 1000px;
    height: 572px;
    border-radius: 34px;
    overflow: hidden;
    box-shadow: 0 14px 40px rgba(0,0,0,0.25);
    background: var(--pattern-light);
  }
  .pattern-field {
    position: absolute;
    left: 0;
    width: 100%;
    height: 180px;
    background:
      radial-gradient(ellipse at 18% 40%, var(--pattern-mid) 0, transparent 45%),
      radial-gradient(ellipse at 55% 60%, var(--pattern-dark) 0, transparent 35%),
      radial-gradient(ellipse at 85% 35%, var(--pattern-mid) 0, transparent 45%),
      linear-gradient(135deg, #e2e2e2, var(--pattern-light) 50%, #cfcfcf);
  }
  .pattern-field.top { top: 0; }
  .pattern-field.bottom { bottom: 0; }
  .band {
    position: absolute;
    left: 0;
    right: 0;
    top: 180px;
    height: 212px;
    background: linear-gradient(100deg, var(--band-dark) 0%, var(--band-mid) 45%, var(--band-dark) 100%);
    display: flex;
    flex-direction: column;
    align-items: center;
    justify-content: center;
    gap: 16px;
  }
  .band::before,
  .band::after {
    content: "";
    position: absolute;
    left: 0;
    right: 0;
    height: 2px;
    background: var(--rule);
  }
  .band::before { top: 16px; }
  .band::after { bottom: 16px; }
  .name {
    font-family: "Great Vibes", cursive;
    font-size: 72px;
    line-height: 1;
    word-spacing: 14px;
    color: var(--text-light);
    margin: 0;
    font-weight: 400;
  }
  .contact {
    font-family: "Open Sans", sans-serif;
    font-size: 22px;
    color: var(--text-light);
    letter-spacing: 0.3px;
    margin: 0;
    white-space: nowrap;
  }
  .contact .sep { margin: 0 10px; }
</style>
</head>
<body>
  <main class="canvas">
    <article class="card">
      <div class="pattern-field top" role="img" aria-label="Black, grey and white leopard-spot animal print pattern"></div>
      <section class="band">
        <h1 class="name">Nora Pettigrew</h1>
        <p class="contact">505-771-4926<span class="sep">|</span>norapettigrew@quillmail.net<span class="sep">|</span>Marrow Creek, NM</p>
      </section>
      <div class="pattern-field bottom" role="img" aria-label="Black, grey and white leopard-spot animal print pattern"></div>
    </article>
  </main>
</body>
</html>
```